New home full landscape package

We have a landscape construction company and have built a new home landscape package and wish to have it on a double sided a5 brochure for us to leave with sales agents. I have attached everything i can think off that would need to be incorporated and am accessible to answer any questions required.

Target Market(s)

new home buyers

Industry/Entity Type

Landscaping

Requirements
Must have
• highlighting $9990 + gst component
• clear directive/ outcome for clients
• 'whats in it for them' feel
Nice to have
• simple, elegant, clean
Should not have
• not be too busy

```html
<!DOCTYPE html>
<html lang="en">
<head>
<meta charset="utf-8">
<title>Verdale – Full Landscape Package Brochure</title>
<link href="https://fonts.googleapis.com/css2?family=Fira+Sans:wght@400;500;600&display=swap" rel="stylesheet">
<style>
:root{
  --green:#a8cb38;
  --orange:#f39322;
  --ink:#2f2f2f;
  --grey:#555;
  --panel:#f3f3f3;
  --bg:#e9e7e3;
  --white:#fff;
}
*{box-sizing:border-box;margin:0;padding:0}
html,body{width:1200px;height:1149px;overflow:hidden}
body{background:var(--bg);font-family:'Fira Sans',sans-serif;color:var(--ink);position:relative}
.card{position:absolute;width:679px;height:484px;background:var(--white);box-shadow:0 2px 8px rgba(0,0,0,.18);overflow:hidden}
.front{left:74px;top:66px}
.back{left:430px;top:568px}

/* front */
.hero{position:absolute;left:17px;top:18px;width:500px;height:361px;
  background:linear-gradient(180deg,#3d5a86 0%,#8da3bf 35%,#d7d2c8 62%,#b7a38d 80%,#5f8a3a 100%)}
.hero-title{position:absolute;left:16px;top:12px;font-size:19px;font-weight:600;color:var(--white);letter-spacing:.2px}
.hero-title span{color:var(--orange);border-bottom:1.5px solid var(--orange)}
.front-foot{position:absolute;left:17px;top:379px;width:500px;height:87px;display:flex;align-items:center}
.brand{display:flex;align-items:center;gap:8px;font-size:27px;font-weight:500;color:var(--grey);letter-spacing:.5px}
.brand i{display:block;width:22px;height:22px;background:var(--green)}
.front-foot .brand{width:250px;padding-left:14px}
.divider{width:1px;height:68px;background:#ccc;margin-right:24px}
.cta{font-size:19px;font-weight:600;color:var(--orange);line-height:1.2}
.front-side{position:absolute;left:517px;top:0;width:162px;height:484px;background:var(--green);padding:16px 10px 0 13px;color:var(--white)}
.front-side h2{font-size:17.5px;font-weight:600;line-height:1.22}
.front-side .price{font-size:21px;font-weight:600;margin-top:4px;text-shadow:0 1px 2px rgba(0,0,0,.25)}
.ticks{list-style:none;margin-top:36px}
.ticks li{position:relative;padding-left:15px;font-size:9.3px;line-height:1.3;color:var(--ink);margin-bottom:6px}
.ticks svg{position:absolute;left:0;top:1px;width:10px;height:10px}

/* back */
.back-side{position:absolute;left:0;top:0;width:162px;height:484px;background:var(--green);color:var(--white)}
.back-side h2{font-size:17.5px;font-weight:600;line-height:1.22;padding:18px 10px 0 16px;height:180px}
.garden{height:226px;background:linear-gradient(180deg,#9cc2e8 0%,#c7b78e 30%,#6f8a4a 55%,#6aa84a 75%,#b8b2a6 100%)}
.back-side .price{text-align:center;font-size:21px;font-weight:600;line-height:1.2;padding-top:14px;text-shadow:0 1px 2px rgba(0,0,0,.25)}
.box{position:absolute;background:var(--panel)}
.box h3{background:var(--orange);color:var(--white);font-size:15px;font-weight:500;padding:4px 8px;line-height:1.25}
.box ul{list-style:none;padding:8px 8px 0 10px}
.box li{position:relative;padding-left:16px;font-size:10.2px;line-height:1.5;color:var(--ink)}
.box li::before{content:"";position:absolute;left:1px;top:5px;width:7px;height:7px;border-radius:50%;background:var(--green);box-shadow:inset -1px -1px 0 #6f8f1f}
.box p{font-size:10.5px;line-height:1.45;padding:10px 12px}
.box .solo{position:absolute;inset:0;display:flex;align-items:center;justify-content:center;color:var(--orange);font-size:14px}
.back-foot{position:absolute;left:178px;top:392px;width:490px;height:72px;display:flex;align-items:center}
.back-foot .brand{width:220px;padding-left:2px}
.badge{width:72px;height:44px;border:2px solid #2c6fb3;border-radius:4px;background:#eef4fa;margin-right:24px;position:relative}
.badge::after{content:"";position:absolute;left:0;right:0;bottom:0;height:9px;background:var(--green)}
.back-foot .cta{font-size:16px}
</style>
</head>
<body>

<section class="card front">
  <div class="hero" role="img" aria-label="Photo of a modern two-storey new home at dusk with a fresh front lawn">
    <h1 class="hero-title">VERDALE – <span>FULL LANDSCAPE PACKAGE</span></h1>
  </div>
  <div class="front-foot">
    <div class="brand"><i></i>VERDALE</div>
    <div class="divider"></div>
    <p class="cta">Speak to us today to<br>organize your free<br>quote</p>
  </div>
  <aside class="front-side">
    <h2>Create your outdoor space with our landscape packages starting from</h2>
    <p class="price">$9,990+GST</p>
    <ul class="ticks">
      <li><svg viewBox="0 0 10 10"><circle cx="5" cy="5" r="4.3" fill="none" stroke="#2f2f2f" stroke-width="1"/><path d="M2.8 5.2l1.6 1.6 3-3.4" fill="none" stroke="#2f2f2f" stroke-width="1.3"/></svg>Inclusions - Everything you need to love your outdoor space</li>
      <li><svg viewBox="0 0 10 10"><circle cx="5" cy="5" r="4.3" fill="none" stroke="#2f2f2f" stroke-width="1"/><path d="M2.8 5.2l1.6 1.6 3-3.4" fill="none" stroke="#2f2f2f" stroke-width="1.3"/></svg>Site consultation including a measure and quote</li>
      <li><svg viewBox="0 0 10 10"><circle cx="5" cy="5" r="4.3" fill="none" stroke="#2f2f2f" stroke-width="1"/><path d="M2.8 5.2l1.6 1.6 3-3.4" fill="none" stroke="#2f2f2f" stroke-width="1.3"/></svg>Site preparation and clearing</li>
      <li><svg viewBox="0 0 10 10"><circle cx="5" cy="5" r="4.3" fill="none" stroke="#2f2f2f" stroke-width="1"/><path d="M2.8 5.2l1.6 1.6 3-3.4" fill="none" stroke="#2f2f2f" stroke-width="1.3"/></svg>New turf including premium soil installed to front &amp; back yards</li>
      <li><svg viewBox="0 0 10 10"><circle cx="5" cy="5" r="4.3" fill="none" stroke="#2f2f2f" stroke-width="1"/><path d="M2.8 5.2l1.6 1.6 3-3.4" fill="none" stroke="#2f2f2f" stroke-width="1.3"/></svg>River rock to sides of house</li>
      <li><svg viewBox="0 0 10 10"><circle cx="5" cy="5" r="4.3" fill="none" stroke="#2f2f2f" stroke-width="1"/><path d="M2.8 5.2l1.6 1.6 3-3.4" fill="none" stroke="#2f2f2f" stroke-width="1.3"/></svg>Feature garden bed</li>
      <li><svg viewBox="0 0 10 10"><circle cx="5" cy="5" r="4.3" fill="none" stroke="#2f2f2f" stroke-width="1"/><path d="M2.8 5.2l1.6 1.6 3-3.4" fill="none" stroke="#2f2f2f" stroke-width="1.3"/></svg>Rubbish removal, clean and watering</li>
      <li><svg viewBox="0 0 10 10"><circle cx="5" cy="5" r="4.3" fill="none" stroke="#2f2f2f" stroke-width="1"/><path d="M2.8 5.2l1.6 1.6 3-3.4" fill="none" stroke="#2f2f2f" stroke-width="1.3"/></svg>Customised options available</li>
    </ul>
  </aside>
</section>

<section class="card back">
  <aside class="back-side">
    <h2>Create your dream lifestyle and show off your personal style with our customized options!</h2>
    <div class="garden" role="img" aria-label="Photos of a landscaped family home and a curved paved garden path through lawn"></div>
    <p class="price">$9,990+GST<br>component</p>
  </aside>

  <div class="box" style="left:179px;top:22px;width:150px;height:136px">
    <h3>Turf Options</h3>
    <ul><li>Wintergreen</li><li>Aussie Blue Couch</li><li>Sir Roland</li><li>Regal Zoysia</li><li>TerraTuff</li><li>Rocks</li></ul>
  </div>
  <div class="box" style="left:339px;top:22px;width:156px;height:136px">
    <h3>Rocks, Pebbles &amp; Paving</h3>
    <p>Choose from our extensive options of rocks, paving, steppers</p>
  </div>
  <div class="box" style="left:506px;top:22px;width:152px;height:136px">
    <h3>Other</h3>
    <ul><li>Mail box</li><li>Clothesline</li><li>Wheelie Bins Paver Slab</li><li>Drainage</li><li>Decking – Porch Entry</li><li>Decking – Custom Decks</li></ul>
  </div>
  <div class="box" style="left:179px;top:168px;width:150px;height:196px">
    <h3>Edging</h3>
    <ul><li>Timber Rail</li><li>Aluminium</li><li>Steel</li><li>Concrete Sleeper</li><li>Timber Sleeper (150mm, 200mm or Stained)</li><li>Paved edges</li><li>Masonry</li><li>Plankwood/Plastic</li></ul>
  </div>
  <div class="box" style="left:339px;top:168px;width:156px;height:74px">
    <h3>Planting</h3>
    <ul><li>Custom plant selection</li><li>Additional Garden beds</li></ul>
  </div>
  <div class="box" style="left:506px;top:168px;width:152px;height:74px">
    <h3>Concrete</h3>
    <ul><li>Concrete – Driveways, Paths &amp; Patios</li></ul>
  </div>
  <div class="box" style="left:339px;top:251px;width:156px;height:113px">
    <h3>Fencing</h3>
    <ul><li>Timber Butt fence</li><li>Glass Pool Fencing</li><li>Good Neighbour</li><li>Steelbond</li><li>Aluminium</li></ul>
  </div>
  <div class="box" style="left:506px;top:251px;width:152px;height:113px">
    <span class="solo">Decking</span>
  </div>

  <div class="back-foot">
    <div class="brand"><i></i>VERDALE</div>
    <div class="divider"></div>
    <div class="badge" aria-label="Industry association member badge"></div>
    <p class="cta">Visit our website<br>for more ideas!</p>
  </div>
</section>

</body>
</html>
```